Tallwren Learning Graphic Design Project

I need graphic design elements to establish a look and feel for my company, Tallwren Learning. I work with companies and organizations who are either starting out in eLearning and need direction or have been at it for a while and could do it better. I work inside the organization to analyse their current learning, devise strategic plans and then stay around to help implement them. This saves the organization a lot of money and gives them happier and more able workers.
I have been working in this industry for many years and see the need for a very specific consultancy focused on the strategies behind adult learning offerings that involve screens (this is almost all).
Tallwren thinks outside the box. But it also follows up with concrete results. Surprising things can be achieved. This is the kind of feeling I'd like to convey in the Tallwren look and feel. So I'm looking for a set of graphic elements that can be used mainly for business cards and website objects. To give you an idea of the style of thing I like I have attached a business card template that I like. What I like is its freshness and clarity. But open to all ideas. Thanks and good luck.
Updates

 I've posted a new image  to show what I mean by clean and fresh. Not suggesting that I need a cord with a knot in it but I really like the colour, contrast and sort of starkness of the image. Suggesting this as apossible direction change to use with those good ideas already submitted and to help clarify for new ones. Thanks again.

                                   

Target Market(s)

corporates and larger organizations - any organization that has or wants to have elearning in their training mix.

Industry/Entity Type

Graphic Design

Requirements
Must have
• elements that can be used to create a website, business cards, other materials as required. So this might include a font recommendation and a number of illustrations that can be used together or separately.
Nice to have
• nice if you could include the elements designed as a business card in a ready-to-print format.
Should not have
• don't really want a logo in the usual sense

```html
<!DOCTYPE html>
<html lang="en">
<head>
<meta charset="utf-8">
<title>Tallwren Learning — Business Cards</title>
<link href="https://fonts.googleapis.com/css2?family=Quicksand:wght@400;500;600&display=swap" rel="stylesheet">
<style>
  :root {
    --sky-deep: #0f86c6;
    --sky: #1e9ad6;
    --sky-light: #3aaee2;
    --band: #1b88c8;
    --ink: #1c1c1c;
    --paper: #ffffff;
    --backdrop: #ece9e4;
    --lime: #86c33a;
    --sun: #e2d31c;
    --navy: #1a1f66;
    --magenta: #d2177f;
    --tangerine: #e8631c;
  }
  * { box-sizing: border-box; margin: 0; padding: 0; }
  html, body { width: 1200px; height: 720px; overflow: hidden; }
  body {
    background: var(--backdrop);
    font-family: "Quicksand", sans-serif;
    position: relative;
  }
  .card {
    position: absolute;
    top: 205px;
    width: 540px;
    height: 310px;
    overflow: hidden;
  }
  .card--front {
    left: 40px;
    background: linear-gradient(160deg, var(--sky-light) 0%, var(--sky) 50%, var(--sky-deep) 100%);
  }
  .card--back { left: 620px; background: var(--paper); }

  .artwork {
    position: absolute;
    top: 0;
    height: 100%;
    background: linear-gradient(135deg, var(--lime) 0%, var(--sun) 35%, var(--magenta) 65%, var(--navy) 100%);
    opacity: 0.85;
  }
  .card--front .artwork { left: 330px; width: 210px; }
  .card--back .artwork { left: 0; width: 300px; }

  .front-title {
    position: absolute;
    left: 22px;
    top: 130px;
    color: var(--paper);
    font-size: 22px;
    font-weight: 500;
    letter-spacing: 0.5px;
  }
  .rule {
    position: absolute;
    left: 0;
    width: 100%;
    height: 2px;
    background: var(--paper);
  }
  .rule--top { top: 164px; }
  .rule--bottom { top: 197px; }
  .front-band {
    position: absolute;
    left: 0;
    top: 167px;
    width: 100%;
    height: 28px;
    background: var(--sky-light);
  }
  .tagline {
    position: absolute;
    left: 24px;
    top: 171px;
    color: var(--paper);
    font-size: 14px;
    font-style: italic;
    letter-spacing: 0.5px;
  }
  .front-url {
    position: absolute;
    left: 30px;
    top: 266px;
    color: var(--paper);
    font-size: 16px;
    letter-spacing: 0.8px;
  }

  .back-band {
    position: absolute;
    left: 0;
    top: 78px;
    width: 100%;
    height: 24px;
    background: var(--band);
  }
  .identity {
    position: absolute;
    right: 40px;
    top: 30px;
    text-align: left;
  }
  .identity__name {
    color: var(--band);
    font-size: 20px;
    font-weight: 500;
    letter-spacing: 0.5px;
  }
  .identity__role {
    color: var(--ink);
    font-size: 12px;
    font-weight: 500;
    margin-top: 1px;
    padding-left: 10px;
  }
  .contact {
    position: absolute;
    left: 340px;
    top: 132px;
    list-style: none;
    color: var(--ink);
    font-size: 14px;
    font-weight: 500;
    line-height: 23px;
    text-align: right;
  }
  .contact__brand { color: var(--band); }
</style>
</head>
<body>
  <section class="card card--front" aria-label="Business card front">
    <div class="artwork" role="img" aria-label="Interwoven coloured ribbon illustration with a magenta knot"></div>
    <div class="front-band"></div>
    <div class="rule rule--top"></div>
    <div class="rule rule--bottom"></div>
    <h1 class="front-title">Tallwren Learning</h1>
    <p class="tagline">never stop creating, never stop learning</p>
    <p class="front-url">www.tallwren.net.au</p>
  </section>

  <section class="card card--back" aria-label="Business card back">
    <div class="artwork" role="img" aria-label="Interwoven coloured ribbon illustration with a magenta knot"></div>
    <div class="back-band"></div>
    <div class="identity">
      <p class="identity__name">Maren Holt</p>
      <p class="identity__role">eLearning strategist</p>
    </div>
    <ul class="contact">
      <li>0491 570 156</li>
      <li>maren@tallwren.net.au</li>
      <li>www.<span class="contact__brand">tallwren</span>.net.au</li>
    </ul>
  </section>
</body>
</html>
```